Agarwood Oud Label Design

I need a circular product label designed for an Agarwood or Bakhoor product. I will provide a rich color scheme picture, as well as the company logo. It may be easier to play with different angles of the logo. So, they are attached also. Label should be 56mm diameter circle label.

```html
<!DOCTYPE html>
<html lang="en">
<head>
<meta charset="utf-8">
<title>Velvet Oud House – Round Labels</title>
<link href="https://fonts.googleapis.com/css2?family=Cormorant+Garamond:wght@500&display=swap" rel="stylesheet">
<style>
  :root {
    --backdrop: #e6e6e6;
    --gold: #c9a46a;
    --plum-top: #3a2757;
    --plum: #2e1f45;
    --plum-deep: #1d1526;
    --garnet-top: #7a1f1f;
    --garnet: #5e1a17;
    --garnet-deep: #4a1412;
  }
  html, body {
    margin: 0;
    padding: 0;
    width: 949px;
    height: 1200px;
    overflow: hidden;
    background: var(--backdrop);
  }
  .sheet {
    position: relative;
    width: 949px;
    height: 1200px;
  }
  .label {
    position: absolute;
    display: block;
  }
  .label--plum-upper   { left: 98px;  top: 225px; width: 352px; height: 352px; }
  .label--garnet-upper { left: 551px; top: 188px; width: 318px; height: 318px; }
  .label--plum-lower   { left: 71px;  top: 681px; width: 392px; height: 392px; }
  .label--garnet-lower { left: 511px; top: 599px; width: 360px; height: 360px; }
  .brand-name {
    font-family: "Cormorant Garamond", serif;
    font-weight: 500;
    font-size: 50px;
    fill: var(--gold);
  }
</style>
</head>
<body>
<main class="sheet">

  <svg width="0" height="0" style="position:absolute" aria-hidden="true">
    <defs>
      <clipPath id="disc"><circle cx="200" cy="200" r="200"/></clipPath>
      <clipPath id="above-wave"><path d="M0,0 H400 V170 C270,228 130,238 0,165 Z"/></clipPath>
      <linearGradient id="plum-body" x1="0" y1="0" x2="0" y2="1">
        <stop offset="0" stop-color="#3a2757"/>
        <stop offset="0.6" stop-color="#2e1f45"/>
        <stop offset="1" stop-color="#1d1526"/>
      </linearGradient>
      <linearGradient id="garnet-body" x1="0" y1="0" x2="0" y2="1">
        <stop offset="0" stop-color="#7a1f1f"/>
        <stop offset="0.6" stop-color="#5e1a17"/>
        <stop offset="1" stop-color="#4a1412"/>
      </linearGradient>
      <radialGradient id="ornament-tone" cx="200" cy="225" r="185" gradientUnits="userSpaceOnUse">
        <stop offset="0" stop-color="#140d0c"/>
        <stop offset="0.4" stop-color="#4a3522"/>
        <stop offset="0.8" stop-color="#a9844f"/>
        <stop offset="1" stop-color="#c9a46a"/>
      </radialGradient>
      <g id="label-face">
        <path d="M22,225 A178,178 0 0 1 378,225 Z" fill="url(#ornament-tone)" clip-path="url(#above-wave)" role="img" aria-label="Gold mandala ornament, half-circle, across the top of the label"/>
        <path d="M0,165 C130,238 270,228 400,170" fill="none" stroke="var(--gold)" stroke-width="1.5"/>
        <text class="brand-name" x="100" y="282">Velvet Oud</text>
        <text class="brand-name" x="160" y="330">House</text>
      </g>
    </defs>
  </svg>

  <svg class="label label--plum-upper" viewBox="0 0 400 400" aria-label="Velvet Oud House label, plum">
    <g clip-path="url(#disc)">
      <rect width="400" height="400" fill="url(#plum-body)"/>
      <use href="#label-face"/>
    </g>
  </svg>

  <svg class="label label--garnet-upper" viewBox="0 0 400 400" aria-label="Velvet Oud House label, garnet">
    <g clip-path="url(#disc)">
      <rect width="400" height="400" fill="url(#garnet-body)"/>
      <use href="#label-face"/>
    </g>
  </svg>

  <svg class="label label--plum-lower" viewBox="0 0 400 400" aria-label="Velvet Oud House label, plum">
    <g clip-path="url(#disc)">
      <rect width="400" height="400" fill="url(#plum-body)"/>
      <use href="#label-face"/>
    </g>
  </svg>

  <svg class="label label--garnet-lower" viewBox="0 0 400 400" aria-label="Velvet Oud House label, garnet">
    <g clip-path="url(#disc)">
      <rect width="400" height="400" fill="url(#garnet-body)"/>
      <use href="#label-face"/>
    </g>
  </svg>

</main>
</body>
</html>
```